Dental specialist needs a sharp looking letterhead

I am looking for a letterhead to be used to send letters and communication between myself (a dental specialist) and other dentists.
My office is a state of the art dental specialty office.
I need to letterhead to also state:
Gideon R. Whitfield DDS
2847 Birchmont Avenue, Suite K
West Harlow, NY 14391
(716)482-9163
fax: (716)482-9170
whitfieldroot.com (**this email address may change)

i included my logo designs.
thank you

Target Market(s)

dentists

Industry/Entity Type

Communication

Requirements
Must have
• the included logo, whether the vertical or horizontal versions

```html
<!DOCTYPE html>
<html lang="en">
<head>
<meta charset="utf-8">
<title>Crestline Endodontics P.C. — Letterhead</title>
<link href="https://fonts.googleapis.com/css2?family=Open+Sans:wght@400;600;700&display=swap" rel="stylesheet">
<style>
  :root {
    --backdrop: #a9aaac;
    --paper: #ffffff;
    --header-band: #dde8f4;
    --ink: #1f2328;
    --ink-soft: #3d434a;
    --brand-mark: #3aa6c9;
    --rule: #2b2f33;
  }
  * { box-sizing: border-box; margin: 0; padding: 0; }
  html, body {
    width: 1200px;
    height: 1200px;
    overflow: hidden;
    background: var(--backdrop);
    font-family: "Open Sans", Arial, sans-serif;
    color: var(--ink);
  }
  .canvas {
    width: 1200px;
    height: 1200px;
    display: flex;
    align-items: center;
    justify-content: center;
  }
  .letterhead {
    position: relative;
    width: 850px;
    height: 1100px;
    background: var(--paper);
    box-shadow: 0 6px 22px rgba(0,0,0,0.25);
  }
  .header-band {
    position: absolute;
    top: 0; left: 0; right: 0;
    height: 130px;
    background: var(--header-band);
    display: flex;
    align-items: center;
    justify-content: space-between;
    padding: 0 70px 0 56px;
  }
  .brand {
    display: flex;
    align-items: center;
    gap: 16px;
  }
  .brand-mark {
    width: 44px;
    height: 44px;
    border-radius: 50%;
    background: var(--brand-mark);
    flex: none;
  }
  .brand-name {
    font-weight: 700;
    color: var(--ink);
    line-height: 1.05;
  }
  .brand-name .primary {
    display: block;
    font-size: 34px;
    letter-spacing: 1px;
    text-transform: uppercase;
  }
  .brand-name .secondary {
    display: block;
    font-size: 18px;
    letter-spacing: 1.5px;
  }
  .sender-address {
    font-style: normal;
    font-size: 12.5px;
    line-height: 1.5;
    color: var(--ink-soft);
  }
  .sender-address .doctor {
    font-weight: 600;
    color: var(--ink);
  }
  .footer-contacts {
    position: absolute;
    left: 100px;
    right: 70px;
    bottom: 78px;
    border-top: 1.5px solid var(--rule);
    padding-top: 10px;
    display: flex;
    justify-content: space-around;
    font-size: 12px;
    font-weight: 600;
    color: var(--ink);
  }
  .footer-contacts .label {
    font-weight: 700;
    margin-right: 6px;
  }
</style>
</head>
<body>
  <main class="canvas">
    <article class="letterhead">
      <header class="header-band">
        <div class="brand">
          <span class="brand-mark"></span>
          <span class="brand-name">
            <span class="primary">Crestline</span>
            <span class="secondary">Endodontics P.C.</span>
          </span>
        </div>
        <address class="sender-address">
          <span class="doctor">Gideon R. Whitfield DDS</span><br>
          2847 Birchmont Avenue, Suite K<br>
          West Harlow, NY 14391
        </address>
      </header>

      <footer class="footer-contacts">
        <span class="contact-phone"><span class="label">P</span>(716)482-9163</span>
        <span class="contact-fax"><span class="label">F</span>(716)482-9170</span>
        <span class="contact-web"><span class="label">E</span>whitfieldroot.com</span>
      </footer>
    </article>
  </main>
</body>
</html>
```